Redgate Business Card Design

We are a new small business specialising in under ground cable jointing and excavation works in NSW Australia.
Design I'm looking for is incorporating the Australian flag & excavator with out being to cheesy.
Maybe a faded washed out flag to help with overload of colour? & so its not the main focus.
Very open to creative out of the box designs!

Target Market(s)

Building & Construction

Industry/Entity Type

Construction

Contact Information for Business Card

Redgate Cable Jointing & Excavations
Colin Barwick

Ph: 0412 938 560
E: colin.barwick@tellnet.example

Reverse Side
Services we offer:
High Voltage & Low Voltage Cable Jointing
Polymeric & paperlead jointing & terminations
Trenching & Auger Drilling 150 - 600mm
Site preparation / leveling / clearing
Driveway / Footpath / Turf Prep
Rubbish Removal
Tree & Stump removal
Footings & Post holes
Drainage
Service Installs
Gravels & Sands available
Any general Earth moving needs
Reliable Free Quotes
Fully Insured

Font styles to use
Serif
Script

Requirements
Nice to have
• small excavator (See uploaded picture)

```html
<!DOCTYPE html>
<html lang="en">
<head>
<meta charset="utf-8">
<title>Redgate Business Card Design</title>
<link rel="stylesheet" href="https://fonts.googleapis.com/css2?family=Comfortaa:wght@400;600;700&display=swap">
<style>
:root{
  --navy:#2d3794;
  --red:#e3262c;
  --pale-top:#e4deec;
  --pale-bottom:#f6ddd9;
  --flag-blue:#b7b5d6;
  --flag-red:#f0b9b9;
  --stage:#e9e7e3;
  --ink:#2d3794;
}
*{box-sizing:border-box;margin:0;padding:0}
html,body{width:1200px;height:952px;overflow:hidden}
body{background:var(--stage);font-family:'Comfortaa',sans-serif;color:var(--ink);position:relative}
.card{position:absolute;width:630px;height:365px;overflow:hidden;
  background:linear-gradient(180deg,var(--pale-top) 0%,var(--pale-bottom) 70%);
  box-shadow:0 12px 28px rgba(0,0,0,.25)}
.card--front{left:110px;top:60px}
.card--back{left:470px;top:500px}
.flag-wash{position:absolute;left:0;top:0;width:380px;height:200px;
  background:linear-gradient(135deg,var(--flag-blue) 0%,var(--flag-red) 45%,rgba(255,255,255,0) 100%);opacity:.7}
.band{position:absolute;left:0;bottom:0;width:100%;height:90px}
.wordmark{position:absolute;display:flex;align-items:center;gap:12px;color:var(--navy);
  font-weight:700;font-size:22px;line-height:1.15}
.wordmark__mark{width:26px;height:26px;background:var(--navy);flex:none}
.card--front .wordmark{left:230px;top:42px;width:380px}
.card--back .wordmark{left:250px;top:40px;width:360px}
.holder{position:absolute;left:30px;top:170px;width:570px;display:flex;align-items:flex-end;gap:8px}
.holder__name{font-size:24px;font-weight:600;white-space:nowrap}
.holder__rule{flex:1;height:1px;background:var(--navy);margin-bottom:6px}
.contact{position:absolute;left:335px;top:198px;font-size:15px;line-height:28px;list-style:none}
.contact li{display:flex;align-items:center;gap:10px;white-space:nowrap}
.contact svg{width:17px;height:17px;flex:none}
.roo{position:absolute;width:54px;height:32px;background:var(--red);opacity:.85;border-radius:40% 60% 30% 50%}
.card--front .roo{right:20px;top:250px}
.card--back .roo{right:14px;top:270px}
.services-title{position:absolute;left:30px;top:100px;width:580px;display:flex;align-items:flex-end;gap:8px;font-size:19px;font-weight:700}
.services-title span{flex:1;height:1px;background:var(--navy);margin-bottom:5px}
.services{position:absolute;top:132px;font-size:12.5px;line-height:19px;list-style:none}
.services li{display:flex;align-items:center;gap:8px;white-space:nowrap}
.services li::before{content:"";width:0;height:0;border-left:8px solid var(--red);border-top:4px solid transparent;border-bottom:4px solid transparent}
.services--left{left:30px}
.services--right{left:380px;top:140px}
.band-phone{position:absolute;left:0;bottom:22px;width:100%;display:flex;justify-content:center;align-items:center;gap:10px;color:#fff;font-size:17px}
.band-phone svg{width:18px;height:18px}
</style>
</head>
<body>

<section class="card card--front">
  <div class="flag-wash" role="img" aria-label="Faded Australian flag wash"></div>
  <div class="wordmark"><span class="wordmark__mark"></span><span>Redgate Cable Jointing &amp; Excavations</span></div>
  <div class="holder"><span class="holder__name">Colin Barwick</span><span class="holder__rule"></span></div>
  <ul class="contact">
    <li><svg viewBox="0 0 24 24"><path fill="#2d3794" d="M3 9c0-3 4-5 9-5s9 2 9 5v2h-5V8H8v3H3zM6 12h12l2 8H4z"/></svg>0412 938 560</li>
    <li><svg viewBox="0 0 24 24"><rect x="2" y="5" width="20" height="14" fill="#2d3794"/><path d="M2 5l10 8 10-8" stroke="#fff" stroke-width="1.5" fill="none"/></svg>colin.barwick@tellnet.example</li>
  </ul>
  <svg class="band" viewBox="0 0 630 90" preserveAspectRatio="none">
    <polygon points="0,30 630,0 630,90 0,90" fill="#2d3794"/>
    <polyline points="0,28 630,-2" stroke="#e3262c" stroke-width="4" fill="none"/>
  </svg>
  <div class="roo" role="img" aria-label="Kangaroo silhouette"></div>
</section>

<section class="card card--back">
  <div class="flag-wash" role="img" aria-label="Faded Australian flag wash"></div>
  <div class="wordmark"><span class="wordmark__mark"></span><span>Redgate Cable Jointing &amp; Excavations</span></div>
  <div class="services-title">Services we offer:<span></span></div>
  <ul class="services services--left">
    <li>High Voltage &amp; Low Voltage Cable Jointing</li>
    <li>Polymeric &amp; paperlead jointing &amp; terminations</li>
    <li>Trenching &amp; Auger Drilling 150 - 600mm</li>
    <li>Site preparation / leveling / clearing</li>
    <li>Driveway / Footpath / Turf Prep</li>
    <li>Rubbish Removal</li>
    <li>Tree &amp; Stump removal</li>
  </ul>
  <ul class="services services--right">
    <li>Footings &amp; Post holes</li>
    <li>Drainage</li>
    <li>Service Installs</li>
    <li>Gravels &amp; Sands available</li>
    <li>Any general Earth moving needs</li>
    <li>Reliable Free Quotes</li>
    <li>Fully Insured</li>
  </ul>
  <svg class="band" viewBox="0 0 630 90" preserveAspectRatio="none">
    <polygon points="0,10 630,30 630,90 0,90" fill="#2d3794"/>
    <polyline points="0,8 630,28" stroke="#e3262c" stroke-width="4" fill="none"/>
  </svg>
  <div class="roo" role="img" aria-label="Kangaroo silhouette"></div>
  <div class="band-phone"><svg viewBox="0 0 24 24"><path fill="#e3262c" d="M3 9c0-3 4-5 9-5s9 2 9 5v2h-5V8H8v3H3zM6 12h12l2 8H4z"/></svg>0412 938 560</div>
</section>

</body>
</html>
```